Bright Ridge Electric Needs A Logo Design

We need a logo for my new company based out of Sacramento, Ca called Bright Ridge Electric. The name says it all, my electrical contracting business provides "Bright Ridge Professional Work" I'm open to any colors that pop and customers to say Wow. I would love to print my cards on metal.

Industry/Entity Type

Business

Contact Information for Business Card

The card needs to have as follows
Name of company: Bright Ridge Electric
My Name: Dorian Pelko
Phone # 916-382-5507
CL# 2087396
Email: brightridgeelectric@mailvance.net
and a slogan that represent "BRIGHT RIDGE"

Requirements
Must have
• The card needs to have as follows
• Name of company: Bright Ridge Electric
• My Name : Dorian Pelko
• Phone # 916-382-5507
• CL# 2087396
• Email: brightridgeelectric@mailvance.net
• and a slogan that represent "BRIGHT RIDGE"
Nice to have
• popping colors
• electrical Arcing

```html
<!DOCTYPE html>
<html lang="en">
<head>
<meta charset="utf-8">
<title>Bright Ridge Electric – Business Card</title>
<link rel="stylesheet" href="https://fonts.googleapis.com/css2?family=Aldrich&display=swap">
<style>
  :root {
    --backdrop: #1a1a1a;
    --card-black: #050505;
    --stripe-yellow: #ffe000;
    --body-top: #ffe600;
    --body-bottom: #f08a2a;
    --band-blue: #6f7fd8;
    --brand-blue: #7fa8ec;
    --arc-violet: #7a4fd0;
    --arc-glow: #c59bff;
    --ink: #111111;
  }
  * { box-sizing: border-box; margin: 0; padding: 0; }
  html, body {
    width: 1200px; height: 800px; overflow: hidden;
    background: var(--backdrop);
  }
  .stage {
    width: 1200px; height: 800px;
    display: flex; align-items: center; justify-content: center;
  }
  .business-card {
    position: relative;
    width: 1050px; height: 600px;
    background: var(--card-black);
    overflow: hidden;
    font-family: "Aldrich", sans-serif;
  }
  .brand-area {
    position: absolute; left: 0; top: 0; width: 100%; height: 232px;
  }
  .arc-art {
    position: absolute; right: 0; top: 60px; width: 560px; height: 172px;
    background: radial-gradient(ellipse at 80% 55%, var(--arc-glow) 0%, var(--arc-violet) 25%, rgba(60,30,120,0.35) 55%, rgba(5,5,5,0) 75%);
    opacity: 0.8;
  }
  .arc-art.corner {
    left: 0; right: auto; top: 0; width: 160px; height: 110px;
    background: radial-gradient(ellipse at 20% 20%, var(--arc-glow) 0%, var(--arc-violet) 25%, rgba(5,5,5,0) 70%);
    opacity: 0.6;
  }
  .brand-lockup {
    position: absolute; left: 60px; top: 70px;
    display: flex; align-items: center; gap: 22px;
  }
  .brand-square {
    width: 84px; height: 84px;
    border: 3px solid var(--brand-blue);
  }
  .brand-name {
    color: var(--brand-blue);
    font-size: 48px; letter-spacing: 2px;
    text-transform: uppercase;
  }
  .stripe-yellow {
    position: absolute; left: 0; top: 232px; width: 100%; height: 12px;
    background: var(--stripe-yellow);
  }
  .stripe-black {
    position: absolute; left: 0; top: 244px; width: 100%; height: 6px;
    background: var(--card-black);
  }
  .info-panel {
    position: absolute; left: 0; top: 250px; width: 100%; height: 300px;
    background: linear-gradient(180deg, var(--body-top) 0%, var(--body-bottom) 100%);
  }
  .contact-block {
    position: absolute; left: 0; right: 0; top: 40px;
    text-align: center; color: var(--ink);
    padding-left: 140px;
  }
  .holder-name { font-size: 40px; letter-spacing: 1px; }
  .holder-title { font-size: 24px; margin-top: 4px; }
  .contact-line { font-size: 27px; margin-top: 6px; }
  .band-rule {
    position: absolute; left: 0; top: 550px; width: 100%; height: 6px;
    background: var(--card-black);
  }
  .band-blue {
    position: absolute; left: 0; top: 556px; width: 100%; height: 44px;
    background: var(--band-blue);
  }
</style>
</head>
<body>
<main class="stage">
  <section class="business-card">
    <div class="brand-area">
      <div class="arc-art corner" role="img" aria-label="Violet electric arc illustration"></div>
      <div class="arc-art" role="img" aria-label="Violet lightning bolts arcing across the dark header"></div>
      <div class="brand-lockup">
        <div class="brand-square"></div>
        <span class="brand-name">Bright Ridge Electric</span>
      </div>
    </div>
    <div class="stripe-yellow"></div>
    <div class="stripe-black"></div>
    <div class="info-panel">
      <div class="contact-block">
        <p class="holder-name">DORIAN PELKO</p>
        <p class="holder-title">TITLE HERE</p>
        <p class="contact-line">Phone: #916-382-5507</p>
        <p class="contact-line">CL: #2087396</p>
        <p class="contact-line">Email: brightridgeelectric@mailvance.net</p>
      </div>
    </div>
    <div class="band-rule"></div>
    <div class="band-blue"></div>
  </section>
</main>
</body>
</html>
```